Stationary Package
Business Card / Letterhead / Envelop
I need double sided standard sized Business Card [3.5" x 2"]
use same look and feel font(s)
Professional
Daniel Whitfield
Marketing Strategist
4518 Harwick Crescent
Mississauga, Ontario, L4T 3K8
danielwhitfield@vellorahaus.com
www.vellorahaus.com
design package for the marketing industry
Logo with tag line
plus the website address
Logo and Tag Line
eps logo
pdf logo version

```html
<!DOCTYPE html>
<html lang="en">
<head>
<meta charset="utf-8">
<title>Daniel Whitfield — Stationery Package</title>
<link href="https://fonts.googleapis.com/css2?family=Montserrat:wght@400;600;700&family=Open+Sans:wght@400;600&display=swap" rel="stylesheet">
<style>
  :root{
    --stage:#e8e9ea;
    --paper:#ffffff;
    --brand:#1f86cc;
    --ink:#3a3f44;
    --muted:#8a8f94;
    --cell:#dcdee1;
    --cell-dark:#c6c9cd;
    --ghost:#eef1f4;
    --envelope-fold:#e1e3e6;
    --shadow:0 1px 3px rgba(0,0,0,.18);
  }
  *{box-sizing:border-box;margin:0;padding:0}
  html,body{width:1200px;height:542px;overflow:hidden}
  body{background:var(--stage);font-family:"Open Sans",Arial,sans-serif;color:var(--ink);position:relative}
  .sheet{position:absolute;background:var(--paper);box-shadow:var(--shadow);overflow:hidden}
  .brand{display:flex;flex-direction:column;align-items:flex-start;position:relative;z-index:1}
  .brand-mark{width:12px;height:12px;border-radius:50%;background:var(--brand);margin-bottom:3px}
  .brand-name{font-family:"Montserrat",Arial,sans-serif;font-weight:700;color:var(--brand);font-size:8px;letter-spacing:.4px;white-space:nowrap}
  .brand-tag{font-size:4.5px;color:var(--muted);margin-top:1px}
  .ghost-name{position:absolute;font-family:"Montserrat",Arial,sans-serif;font-weight:700;color:var(--ghost);line-height:1.05;white-space:nowrap;z-index:0}
  .footer-lines{position:absolute;font-size:3.6px;line-height:5px;color:var(--muted);z-index:1}

  /* letterheads */
  .letterhead{top:12px;width:168px;height:518px}
  .letterhead--fax{left:19px}
  .letterhead--plain{left:221px}
  .letterhead .brand{position:absolute;left:14px;top:14px}
  .letterhead .ghost-name{left:12px;top:200px;font-size:26px}
  .letterhead .footer-lines{left:14px;bottom:20px}

  .fax-title{position:absolute;right:36px;top:165px;font-family:"Montserrat",Arial,sans-serif;font-size:5px;font-weight:600;color:var(--ink);z-index:1}
  .fax-table{position:absolute;left:8px;top:172px;width:126px;border-collapse:collapse;font-size:3.8px;z-index:1}
  .fax-table td{height:10px;border:1px solid var(--paper);padding:0 3px}
  .fax-table .label{background:var(--cell-dark);width:14%}
  .fax-table .value{background:var(--cell);width:36%}
  .fax-checks{position:absolute;left:8px;top:240px;width:152px;display:flex;justify-content:space-between;font-size:3.4px;color:var(--ink);z-index:1}
  .fax-checks span{display:flex;align-items:center;gap:1.5px;white-space:nowrap}
  .fax-checks i{width:4px;height:4px;border:.6px solid var(--muted);display:inline-block}

  /* business cards */
  .card{top:34px;width:138px;height:80px;border-radius:4px}
  .card--front{left:427px}
  .card--back{left:584px}
  .card--front .brand{position:absolute;left:9px;top:9px}
  .card-contact{position:absolute;left:9px;top:28px;font-size:3.6px;line-height:5px;color:var(--ink)}
  .card-person{position:absolute;right:10px;top:28px;font-size:3.6px;line-height:5px}
  .card-person strong{font-family:"Montserrat",Arial,sans-serif;color:var(--brand);font-size:4.4px;font-weight:600;display:block}
  .card--back .brand{position:absolute;left:0;right:0;top:24px;align-items:center}
  .card-web{position:absolute;left:0;right:0;bottom:9px;text-align:center;font-size:3.8px;color:var(--muted)}

  /* envelopes */
  .envelope--back{left:432px;top:173px;width:288px;height:140px}
  .envelope--back svg{position:absolute;inset:0}
  .envelope--front{left:408px;top:281px;width:302px;height:156px}
  .envelope--front .brand{position:absolute;left:14px;top:12px}
  .envelope--front .brand-name{font-size:10px}
  .envelope--front .footer-lines{left:14px;top:58px}
  .envelope--front .ghost-name{right:14px;top:84px;font-size:24px}
</style>
</head>
<body>

<section class="sheet letterhead letterhead--fax" aria-label="Fax letterhead">
  <div class="ghost-name">Daniel<br>Whitfield</div>
  <div class="brand">
    <span class="brand-mark"></span>
    <span class="brand-name">DANIEL WHITFIELD</span>
    <span class="brand-tag">Vellora Haus</span>
  </div>
  <div class="fax-title">FAX</div>
  <table class="fax-table">
    <tr><td class="label">To:</td><td class="value"></td><td class="label">From:</td><td class="value"></td></tr>
    <tr><td class="label">Fax:</td><td class="value"></td><td class="label">Pages:</td><td class="value"></td></tr>
    <tr><td class="label">Phone:</td><td class="value"></td><td class="label">Date:</td><td class="value"></td></tr>
    <tr><td class="label">Re:</td><td class="value"></td><td class="label">CC:</td><td class="value"></td></tr>
  </table>
  <div class="fax-checks">
    <span><i></i>Urgent</span>
    <span><i></i>For Review</span>
    <span><i></i>Please Comment</span>
    <span><i></i>Please Reply</span>
    <span><i></i>Please Recycle</span>
  </div>
  <div class="footer-lines">
    4518 Harwick Crescent<br>
    Mississauga, Ontario, L4T 3K8<br>
    danielwhitfield@vellorahaus.com<br>
    www.vellorahaus.com
  </div>
</section>

<section class="sheet letterhead letterhead--plain" aria-label="Letterhead">
  <div class="ghost-name">Daniel<br>Whitfield</div>
  <div class="brand">
    <span class="brand-mark"></span>
    <span class="brand-name">DANIEL WHITFIELD</span>
    <span class="brand-tag">Vellora Haus</span>
  </div>
  <div class="footer-lines">
    4518 Harwick Crescent<br>
    Mississauga, Ontario, L4T 3K8<br>
    danielwhitfield@vellorahaus.com<br>
    www.vellorahaus.com
  </div>
</section>

<section class="sheet card card--front" aria-label="Business card front">
  <div class="brand"><span class="brand-mark"></span></div>
  <div class="card-contact">
    4518 Harwick Crescent<br>
    Mississauga, Ontario, L4T 3K8<br>
    Tel 905 555 0142<br>
    danielwhitfield@vellorahaus.com
  </div>
  <div class="card-person">
    <strong>Daniel Whitfield</strong>
    Marketing Strategist
  </div>
</section>

<section class="sheet card card--back" aria-label="Business card back">
  <div class="brand">
    <span class="brand-mark"></span>
    <span class="brand-name">DANIEL WHITFIELD</span>
    <span class="brand-tag">Vellora Haus</span>
  </div>
  <div class="card-web">www.vellorahaus.com</div>
</section>

<section class="sheet envelope--back" aria-label="Envelope back">
  <svg width="288" height="140" viewBox="0 0 288 140">
    <polyline points="0,0 144,62 288,0" fill="none" stroke="var(--envelope-fold)" stroke-width="1"/>
  </svg>
</section>

<section class="sheet envelope--front" aria-label="Envelope front">
  <div class="ghost-name">Daniel Whitfield</div>
  <div class="brand">
    <span class="brand-mark"></span>
    <span class="brand-name">DANIEL WHITFIELD</span>
    <span class="brand-tag">Vellora Haus</span>
  </div>
  <div class="footer-lines">
    4518 Harwick Crescent<br>
    Mississauga, Ontario, L4T 3K8<br>
    Tel 905 555 0142 &nbsp;Fax 905 555 0143<br>
    www.vellorahaus.com
  </div>
</section>

</body>
</html>
```